Velnoro Powerpoint Templates

Create a Powerpoint Template based on existing logo, colors, mascot with support for the 10-12 most important slides types, default format FullHD re ...

Target Market(s)

Thailand

Industry/Entity Type

Insurance Broker

Font styles to use
Sans Serif

```html
<!DOCTYPE html>
<html lang="en">
<head>
<meta charset="utf-8">
<title>Velnoro Presentation Template</title>
<link rel="stylesheet" href="https://fonts.googleapis.com/css2?family=Open+Sans:wght@400;600;700&display=swap">
<style>
:root{
  --blue:#3a97d4;
  --yellow:#fbc24e;
  --dark:#3e3e3e;
  --ink:#4a4a4a;
  --muted:#8a8a8a;
  --page:#e6e6e6;
  --white:#ffffff;
}
*{box-sizing:border-box;margin:0;padding:0}
html,body{width:1200px;height:686px;overflow:hidden;background:var(--page);font-family:"Open Sans",Arial,sans-serif;color:var(--ink)}
.deck{display:grid;grid-template-columns:repeat(4,292px);grid-auto-rows:164px;gap:6px;padding:4px 7px}
.slide{position:relative;background:var(--white);overflow:hidden}
.abs{position:absolute}
.bar{position:absolute;left:0;right:0;bottom:0;height:6px;background:var(--blue)}
.num{position:absolute;right:6px;bottom:0;font-size:4px;color:var(--white);line-height:6px}
.brand{position:absolute;font-weight:600;color:var(--yellow);display:flex;align-items:center;gap:2px;line-height:1}
.brand i{display:block;border-radius:50%;background:var(--dark)}
.brand-sm{top:5px;right:6px;font-size:6px}
.brand-sm i{width:5px;height:5px}
.title{position:absolute;left:0;right:0;text-align:center;font-size:11.5px;font-weight:600;color:var(--dark)}
.tiny{font-size:3.6px;line-height:1.45;color:var(--ink)}
.photo{position:absolute}
.deck-name{font-weight:700;font-size:17px;letter-spacing:-.2px}
.deck-sub{font-size:8.5px;font-weight:600}
.icon-dot{position:absolute;width:12px;height:12px;border-radius:50%}
.check{font-size:4.4px;color:var(--muted)}
.step{position:absolute;left:166px;width:104px;height:24px;display:flex;gap:5px;overflow:hidden}
.step-num{flex:none;width:13px;height:13px;border-radius:50%;border:1.5px solid var(--yellow);background:#fff;font-size:4.5px;font-weight:700;line-height:1;display:flex;align-items:center;justify-content:center}
.step-title{display:block;font-size:3.8px;line-height:1.3;font-weight:700}
.step-text{font-size:3px;line-height:1.35;color:var(--ink)}
</style>
</head>
<body>
<main class="deck">

  <section class="slide" style="background:var(--blue)">
    <div class="abs" style="left:13px;top:13px;width:268px;height:145px;background:var(--white)"></div>
    <div class="brand" style="left:60px;top:30px;font-size:34px"><i style="width:22px;height:22px;background:var(--blue)"></i>Velnoro</div>
    <div class="abs deck-name" style="left:0;right:0;top:101px;text-align:center;color:var(--yellow)">Your Slides Deck Name</div>
    <div class="abs deck-sub" style="left:0;right:0;top:122px;text-align:center;color:var(--dark)">Your Slides Deck Name</div>
  </section>

  <section class="slide" style="background:var(--yellow)">
    <div class="photo" role="img" aria-label="Toy cars standing on stacks of coins" style="left:13px;top:10px;width:272px;height:138px;background:linear-gradient(160deg,#8b8f96,#5f646c 55%,#7c6f55)"></div>
    <div class="brand" style="left:92px;top:28px;font-size:27px"><i style="width:16px;height:16px;background:var(--blue)"></i>Velnoro</div>
    <div class="abs deck-name" style="left:0;right:0;top:84px;text-align:center;color:var(--white)">Your Slides Deck Name</div>
    <div class="abs deck-sub" style="left:0;right:0;top:104px;text-align:center;color:var(--white)">Your Slides Deck Name</div>
  </section>

  <section class="slide">
    <div class="photo" role="img" aria-label="Cupped hands protecting a red toy car" style="left:0;top:0;width:292px;height:124px;background:linear-gradient(180deg,#b9ad9f,#cdbfae 50%,#e9e2d8)"></div>
    <div class="abs deck-name" style="left:0;right:0;top:62px;text-align:center;color:var(--white)">Your Slides Deck Name</div>
    <div class="abs deck-sub" style="left:0;right:0;top:83px;text-align:center;color:var(--white)">Your Slides Deck Name</div>
    <div class="brand" style="left:103px;top:136px;font-size:20px"><i style="width:12px;height:12px;background:var(--blue)"></i>Velnoro</div>
  </section>

  <section class="slide">
    <div class="photo" role="img" aria-label="Hand sheltering a glowing car symbol" style="inset:0;background:linear-gradient(110deg,#dfe6ee,#c3ced9 60%,#9fb2c4)"></div>
    <svg class="abs" style="inset:0" width="292" height="164" viewBox="0 0 292 164">
      <polygon points="0,75 0,164 65,164" fill="var(--blue)"/>
      <polygon points="0,80 70,164 78,164 0,72" fill="#555"/>
      <polygon points="20,95 60,164 72,164 28,95" fill="var(--yellow)"/>
      <polygon points="210,0 292,0 292,65" fill="var(--blue)"/>
      <polygon points="232,0 246,0 292,42 292,54" fill="var(--yellow)"/>
    </svg>
    <div class="abs" style="left:20px;top:36px;font-size:14px;line-height:1.1;color:var(--blue)">Click to edit<br>Master title style</div>
    <div class="abs" style="left:20px;top:73px;font-size:6.5px;color:var(--blue)">Click to edit Master subtitle style</div>
    <div class="brand" style="right:10px;bottom:8px;font-size:13px">Velnoro<i style="width:8px;height:8px"></i></div>
  </section>

  <section class="slide">
    <div class="brand brand-sm">Velnoro<i></i></div>
    <div class="title" style="top:14px">Lorem ipsum dolor eta</div>
    <div class="photo" role="img" aria-label="Caped superhero mascot in a blue and yellow suit" style="left:6px;top:40px;width:90px;height:110px;background:radial-gradient(circle at 50% 45%,#6aaedb,#c9dbe8 70%,transparent 72%)"></div>
    <p class="abs tiny" style="left:125px;top:38px;width:158px">Lorem ipsum dolor sit amet, consectetur adipiscing elit, sed do eiusmod tempor incididunt ut labore et dolore magna aliqua. Ut enim ad minim veniam, quis nostrud exercitation ullamco laboris nisi ut aliquip ex.</p>
    <div class="abs" style="left:125px;top:70px;width:168px;height:40px;background:var(--yellow)"></div>
    <p class="abs tiny" style="left:130px;top:76px;width:155px">Lorem ipsum dolor sit amet, consectetur adipiscing elit, sed do eiusmod tempor incididunt ut labore et dolore magna aliqua. Ut enim ad minim veniam, quis nostrud exercitation ullamco laboris nisi ut aliquip ex.</p>
    <p class="abs tiny" style="left:125px;top:117px;width:158px">Lorem ipsum dolor sit amet, consectetur adipiscing elit, sed do eiusmod tempor incididunt ut labore et dolore magna aliqua. Ut enim ad minim veniam, quis nostrud exercitation ullamco laboris nisi ut aliquip ex.</p>
    <div class="bar"></div><span class="num">5</span>
  </section>

  <section class="slide">
    <div class="brand brand-sm">Velnoro<i></i></div>
    <div class="title" style="top:14px">Lorem ipsum dolor eta</div>
    <p class="abs tiny" style="left:22px;top:50px;width:132px">Sed ut perspiciatis, unde omnis iste natus error sit voluptatem accusantium doloremque laudantium, totam rem aperiam eaque ipsa, quae ab illo inventore veritatis et quasi architecto beatae vitae dicta sunt, explicabo. Nemo enim ipsam voluptatem, quia voluptas sit, aspernatur aut odit aut fugit, sed quia consequuntur magni dolores eos, qui ratione voluptatem sequi nesciunt, neque porro quisquam est.</p>
    <p class="abs tiny" style="left:22px;top:92px;width:132px">Sed ut perspiciatis, unde omnis iste natus error sit voluptatem accusantium doloremque laudantium, totam rem aperiam eaque ipsa, quae ab illo inventore veritatis et quasi architecto beatae vitae dicta sunt, explicabo. Nemo enim ipsam voluptatem, quia voluptas sit, aspernatur aut odit aut fugit.</p>
    <div class="abs" style="left:175px;top:34px;width:100px;height:116px;border:1.5px solid var(--yellow)"></div>
    <div class="step" style="top:40px"><span class="step-num">01</span><div><b class="step-title">Your Text Here</b><p class="step-text">Lorem ipsum dolor sit amet, consectetur adipiscing elit, sed do eiusmod tempor.</p></div></div>
    <div class="step" style="top:67px"><span class="step-num">02</span><div><b class="step-title">Your Text Here</b><p class="step-text">Lorem ipsum dolor sit amet, consectetur adipiscing elit, sed do eiusmod tempor.</p></div></div>
    <div class="step" style="top:94px"><span class="step-num">03</span><div><b class="step-title">Your Text Here</b><p class="step-text">Lorem ipsum dolor sit amet, consectetur adipiscing elit, sed do eiusmod tempor.</p></div></div>
    <div class="step" style="top:121px"><span class="step-num">04</span><div><b class="step-title">Your Text Here</b><p class="step-text">Lorem ipsum dolor sit amet, consectetur adipiscing elit, sed do eiusmod tempor.</p></div></div>
    <div class="bar"></div><span class="num">6</span>
  </section>

  <section class="slide">
    <div class="photo" role="img" aria-label="Rows of parked cars at a dealership lot" style="inset:0;background:linear-gradient(135deg,#e9b35c,#dba782 45%,#e7dccf)"></div>
    <div class="abs" style="left:78px;top:52px;width:214px;height:56px;background:rgba(58,151,212,.9)"></div>
    <div class="abs" style="left:88px;top:64px;font-size:27px;font-weight:600;color:#fff;line-height:1">01</div>
    <div class="abs" style="left:126px;top:62px;width:1px;height:32px;background:#fff"></div>
    <div class="abs" style="left:134px;top:63px;font-size:10px;color:#fff;line-height:1.3">THE<br>COMPANY</div>
    <div class="abs" style="left:134px;top:92px;font-size:3.4px;color:#fff">This is the subtitle that makes it comprehensible</div>
    <span class="num" style="color:#fff;bottom:2px">7</span>
  </section>

  <section class="slide">
    <div class="title" style="top:16px;left:20px;text-align:left">Lorem ipsum dolor eta</div>
    <div class="photo" role="img" aria-label="Superhero mascot holding a gold coin" style="left:172px;top:4px;width:118px;height:75px;background:radial-gradient(ellipse at 40% 50%,#6aaedb,#d8e6f0 60%,transparent 62%)"></div>
    <div class="abs" style="left:20px;top:42px;width:140px">
      <div style="display:flex;gap:5px;margin-bottom:8px"><span style="flex:none;width:9px;height:9px;border-radius:50%;background:var(--blue);color:#fff;font-size:6px;display:flex;align-items:center;justify-content:center">✓</span><div><b style="font-size:3.8px">Lorem ipsum dolor</b><p class="tiny" style="font-size:3.2px">Lorem ipsum dolor sit amet, on met consectetur adipiscing elit, sed do eiusmod tempor incididunt.</p></div></div>
      <div style="display:flex;gap:5px;margin-bottom:8px"><span style="flex:none;width:9px;height:9px;border-radius:50%;background:var(--blue);color:#fff;font-size:6px;display:flex;align-items:center;justify-content:center">✓</span><div><b style="font-size:3.8px">Lorem ipsum dolor</b><p class="tiny" style="font-size:3.2px">Lorem ipsum dolor sit amet, on met consectetur adipiscing elit, sed do eiusmod tempor incididunt.</p></div></div>
      <div style="display:flex;gap:5px"><span style="flex:none;width:9px;height:9px;border-radius:50%;background:var(--blue);color:#fff;font-size:6px;display:flex;align-items:center;justify-content:center">✓</span><div><b style="font-size:3.8px">Lorem ipsum dolor</b><p class="tiny" style="font-size:3.2px">Lorem ipsum dolor sit amet, on met consectetur adipiscing elit, sed do eiusmod tempor incididunt.</p></div></div>
    </div>
    <div class="abs" style="left:160px;top:86px;width:132px;height:78px;background:var(--blue)"></div>
    <div class="abs" style="width:132px;left:160px;top:88px;text-align:center;font-size:18px;font-weight:700;color:#fff">“</div>
    <p class="abs" style="left:175px;top:108px;width:102px;text-align:center;font-size:4.6px;line-height:1.35;color:#fff">Lorem ipsum dolor sit amet, consectetur adipiscing elit, sed do eiusmod tempor incididunt ut labore et dolore magna aliqua.</p>
    <span class="num">8</span>
  </section>

  <section class="slide">
    <div class="brand brand-sm">Velnoro<i></i></div>
    <div class="title" style="top:14px">Lorem ipsum dolor eta</div>
    <span class="icon-dot" style="left:27px;top:48px;width:16px;height:16px;background:var(--blue)"></span>
    <span class="icon-dot" style="left:27px;top:81px;width:16px;height:16px;background:var(--yellow)"></span>
    <span class="icon-dot" style="left:27px;top:114px;width:16px;height:16px;background:var(--dark)"></span>
    <p class="abs tiny" style="left:50px;top:50px;width:82px">Lorem ipsum dolor sit amet, consectetur adipiscing elit, sed do eiusmod tempor incididunt ut labore et dolore magna aliqua.</p>
    <p class="abs tiny" style="left:50px;top:83px;width:82px">Lorem ipsum dolor sit amet, consectetur adipiscing elit, sed do eiusmod tempor incididunt ut labore et dolore magna aliqua.</p>
    <p class="abs tiny" style="left:50px;top:116px;width:82px">Lorem ipsum dolor sit amet, consectetur adipiscing elit, sed do eiusmod tempor incididunt ut labore et dolore magna aliqua.</p>
    <svg class="abs" style="left:168px;top:40px" width="100" height="100" viewBox="0 0 100 100">
      <g fill="none" stroke-width="20" transform="rotate(-100 50 50)">
        <circle cx="50" cy="50" r="36" stroke="var(--blue)" stroke-dasharray="71 155"/>
        <circle cx="50" cy="50" r="36" stroke="var(--yellow)" stroke-dasharray="0 76 70 80"/>
        <circle cx="50" cy="50" r="36" stroke="var(--dark)" stroke-dasharray="0 151 72 3"/>
      </g>
    </svg>
    <div class="bar"></div><span class="num">9</span>
  </section>

  <section class="slide">
    <div class="brand brand-sm">Velnoro<i></i></div>
    <div class="title" style="top:14px">Comparison</div>
    <div class="abs" style="left:20px;top:36px;font-size:4.5px;color:var(--blue)">DO'S</div>
    <div class="abs" style="right:22px;top:36px;font-size:4.5px;color:var(--yellow)">DON'TS</div>
    <div class="abs" style="left:20px;top:45px;width:252px;height:1px;background:#e4e4e4"></div>
    <div class="abs" style="left:20px;top:63px;width:80px">
      <div class="check" style="display:flex;justify-content:space-between;margin-bottom:13px">This is a sample text <span style="color:var(--blue)">✓</span></div>
      <div class="check" style="display:flex;justify-content:space-between;margin-bottom:13px">This is a sample text <span style="color:var(--blue)">✓</span></div>
      <div class="check" style="display:flex;justify-content:space-between;margin-bottom:13px">This is a sample text <span style="color:var(--blue)">✓</span></div>
      <div class="check" style="display:flex;justify-content:space-between">This is a sample text <span style="color:var(--blue)">✓</span></div>
    </div>
    <div class="abs" style="left:197px;top:63px;width:80px">
      <div class="check" style="margin-bottom:13px"><span style="color:var(--yellow)">✕</span>&nbsp;&nbsp; This is a sample text</div>
      <div class="check" style="margin-bottom:13px"><span style="color:var(--yellow)">✕</span>&nbsp;&nbsp; This is a sample text</div>
      <div class="check" style="margin-bottom:13px"><span style="color:var(--yellow)">✕</span>&nbsp;&nbsp; This is a sample text</div>
      <div class="check"><span style="color:var(--yellow)">✕</span>&nbsp;&nbsp; This is a sample text</div>
    </div>
    <svg class="abs" style="left:110px;top:62px" width="74" height="74" viewBox="0 0 74 74">
      <path d="M37 1 A36 36 0 0 0 37 73 Z" fill="var(--blue)"/>
      <path d="M37 1 A36 36 0 0 1 37 73 Z" fill="var(--yellow)"/>
      <g fill="none" stroke="#fff" stroke-width="1.6"><rect x="17" y="33" width="4" height="10"/><path d="M21 34 l5-8 v5 h6 v10 h-11"/><rect x="53" y="30" width="4" height="10"/><path d="M53 39 l-5 8 v-5 h-6 v-10 h11"/></g>
    </svg>
    <div class="bar"></div><span class="num">10</span>
  </section>

  <section class="slide">
    <div class="brand brand-sm">Velnoro<i></i></div>
    <div class="abs" style="left:0;right:0;top:38px;height:64px;background:var(--yellow)"></div>
    <div class="abs" style="left:60px;top:19px;width:175px;height:114px;border:1.5px solid var(--blue)"></div>
    <p class="abs" style="left:85px;top:54px;width:125px;text-align:center;font-size:6.4px;line-height:1.45;color:#fff">“This is a quote. Words full of wisdom that someone important said and can make the reader get inspired.”</p>
    <div class="abs" style="left:170px;top:104px;font-size:3.6px;color:#fff">—SOMEONE FAMOUS</div>
    <div class="bar"></div><span class="num">11</span>
  </section>

  <section class="slide">
    <div class="brand brand-sm">Velnoro<i></i></div>
    <div class="abs" style="left:0;right:0;top:110px;height:54px;background:var(--blue)"></div>
    <div class="photo" role="img" aria-label="Hand signing a contract beside a red toy car" style="left:11px;top:12px;width:108px;height:142px;background:linear-gradient(160deg,#b7a38c,#e7e1dc 55%,#d6d0cb)"></div>
    <span class="icon-dot" style="left:131px;top:31px;width:17px;height:17px;background:var(--blue)"></span>
    <span class="icon-dot" style="left:131px;top:68px;width:17px;height:17px;background:var(--yellow)"></span>
    <div class="abs" style="left:156px;top:30px;width:126px"><b style="font-size:3.8px">Lorem ipsum dolor</b><p class="tiny" style="font-size:3.2px">Lorem ipsum dolor sit amet, consectetur adipiscing elit, sed do eiusmod tempor incididunt ut labore et dolore magna aliqua. Ut enim ad minim veniam, quis nostrud exercitation.</p></div>
    <div class="abs" style="left:156px;top:67px;width:126px"><b style="font-size:3.8px">Lorem ipsum dolor</b><p class="tiny" style="font-size:3.2px">Lorem ipsum dolor sit amet, consectetur adipiscing elit, sed do eiusmod tempor incididunt ut labore et dolore magna aliqua. Ut enim ad minim veniam, quis nostrud exercitation.</p></div>
    <p class="abs tiny" style="left:129px;top:120px;width:155px;color:#fff;font-size:3.4px">Lorem ipsum dolor sit amet, consectetur adipiscing elit, sed do eiusmod tempor incididunt ut labore et dolore magna aliqua. Ut enim ad minim veniam, quis nostrud exercitation ullamco laboris nisi ut aliquip ex.</p>
    <span class="num">12</span>
  </section>

  <section class="slide">
    <div class="photo" role="img" aria-label="Sunlit rows of new cars at a dealership lot" style="inset:0;background:linear-gradient(160deg,#f2c77a,#b05a47 35%,#4b4b55 70%,#2e2e34)"></div>
    <p class="abs" style="left:12px;top:110px;width:270px;font-size:6.4px;font-weight:600;line-height:1.5;color:#fff">Sed ut perspiciatis, unde omnis iste natus error sit voluptatem accusantium doloremque laudantium, totam rem aperiam eaque ipsa, quae ab illo inventore veritatis et quasi architecto beatae vitae dicta sunt, explicabo. Nemo enim ipsam voluptatem, quia voluptas sit.</p>
    <span class="num" style="bottom:2px">13</span>
  </section>

  <section class="slide">
    <div class="brand brand-sm">Velnoro<i></i></div>
    <div class="title" style="top:14px">Lorem ipsum dolor eta</div>
    <svg class="abs" style="left:22px;top:46px" width="120" height="68" viewBox="0 0 120 68">
      <rect x="6" y="10" width="9" height="52" fill="var(--blue)"/>
      <rect x="34" y="36" width="9" height="26" fill="#c9a255"/>
      <rect x="62" y="26" width="9" height="36" fill="var(--yellow)"/>
      <rect x="90" y="54" width="9" height="8" fill="var(--dark)"/>
      <g fill="#dcdcdc"><rect x="4" y="1" width="13" height="6"/><rect x="32" y="27" width="13" height="6"/><rect x="60" y="17" width="13" height="6"/><rect x="88" y="45" width="13" height="6"/></g>
      <g font-size="3.5" font-family="Open Sans,sans-serif" fill="#444" text-anchor="middle" font-weight="700"><text x="10.5" y="5.5">80</text><text x="38.5" y="31.5">35</text><text x="66.5" y="21.5">55</text><text x="94.5" y="49.5">10</text></g>
      <line x1="0" y1="62" x2="110" y2="62" stroke="#ccc" stroke-width=".5"/>
      <g font-size="2.6" font-family="Open Sans,sans-serif" fill="#888" text-anchor="middle"><text x="10.5" y="67">Category 1</text><text x="38.5" y="67">Category 2</text><text x="66.5" y="67">Category 3</text><text x="94.5" y="67">Category 4</text></g>
    </svg>
    <div class="abs" style="left:14px;top:120px;width:145px;height:34px;background:#eeeeee"></div>
    <span class="icon-dot" style="left:18px;top:126px;background:var(--blue)"></span>
    <span class="icon-dot" style="left:87px;top:126px;background:var(--yellow)"></span>
    <div class="abs" style="left:34px;top:124px;width:50px"><b style="font-size:3.2px;color:var(--blue)">Lorem ipsum dolor</b><p class="tiny" style="font-size:2.8px">Sed ut perspiciatis, unde omnis iste natus error sit voluptatem accusantium.</p></div>
    <div class="abs" style="left:103px;top:124px;width:52px"><b style="font-size:3.2px;color:var(--blue)">Lorem ipsum dolor</b><p class="tiny" style="font-size:2.8px">Sed ut perspiciatis, unde omnis iste natus error sit voluptatem accusantium.</p></div>
    <div class="abs" style="left:176px;top:43px;width:84px;height:84px;border-radius:50%;background:var(--yellow)"></div>
    <div class="abs" style="left:176px;top:66px;width:84px;text-align:center;font-size:21px;font-weight:700;color:#fff;line-height:1">$1.3</div>
    <div class="abs" style="left:176px;top:91px;width:84px;text-align:center;font-size:6px;color:#fff">Million Raising</div>
    <div class="bar"></div><span class="num">14</span>
  </section>

  <section class="slide">
    <div class="brand brand-sm">Velnoro<i></i></div>
    <svg class="abs" style="left:22px;top:40px" width="120" height="78" viewBox="0 0 120 78">
      <path d="M10 0 H86 a10 10 0 0 1 10 10 V46 L112 56 L96 62 V68 a10 10 0 0 1 -10 10 H10 a10 10 0 0 1 -10 -10 V10 a10 10 0 0 1 10 -10 Z" fill="var(--dark)"/>
    </svg>
    <div class="abs" style="left:22px;top:50px;width:96px;text-align:center;font-size:11px;font-weight:600;color:#fff">Get in Touch</div>
    <p class="abs" style="left:28px;top:67px;width:84px;text-align:center;font-size:3.2px;line-height:1.4;color:#fff">Lorem ipsum dolor sit amet, consectetur adipiscing elit, sed do eiusmod tempor incididunt ut labore et dolore magna aliqua. Ut enim ad minim veniam, quis nostrud exercitation ullamco laboris nisi ut aliquip ex ea commodo consequat.</p>
    <div class="abs" style="left:148px;top:30px;font-size:9px;font-weight:600;color:var(--blue)">Marcus Lenn</div>
    <div class="abs" style="left:148px;top:44px;font-size:5.5px;color:var(--yellow)">IT Director</div>
    <svg class="abs" style="left:144px;top:64px" width="14" height="76" viewBox="0 0 14 76">
      <circle cx="7" cy="7" r="6.5" fill="#eef4fa"/><path d="M4 4 l2 -1 l1.5 2.5 l-1 1 a6 6 0 0 0 2.5 2.5 l1 -1 l2.5 1.5 l-1 2 a7 7 0 0 1 -7.5 -7.5z" fill="var(--blue)"/>
      <circle cx="7" cy="31" r="6.5" fill="#eef4fa"/><rect x="3.5" y="28.5" width="7" height="5" fill="var(--blue)"/><path d="M3.5 28.5 l3.5 3 l3.5 -3" fill="none" stroke="#fff" stroke-width=".6"/>
      <circle cx="7" cy="57" r="6.5" fill="#eef4fa"/><g fill="none" stroke="var(--blue)" stroke-width=".7"><circle cx="7" cy="57" r="3.6"/><ellipse cx="7" cy="57" rx="1.6" ry="3.6"/><line x1="3.4" y1="57" x2="10.6" y2="57"/></g>
    </svg>
    <div class="abs" style="left:171px;top:68px;font-size:5.4px;color:var(--dark)">Mobile: 08 10 20 30 40</div>
    <div class="abs" style="left:171px;top:92px;font-size:5.4px;color:var(--dark)">Email: office@velnoro.com</div>
    <div class="abs" style="left:171px;top:118px;font-size:5.4px;color:var(--dark)">WWW.VELNORO.COM</div>
    <div class="abs" style="left:0;right:0;top:143px;text-align:center;font-size:8px;font-weight:600;color:var(--blue)">The ultimate car insurance comparison</div>
    <div class="bar"></div><span class="num">15</span>
  </section>

</main>
</body>
</html>
```